Book Cover Design Project

I am wanting a book cover for an free downloadable e-book called "The 5 Quiet Leaks that will Sink your Venture"
KPW are chartered accountants based in Wellington NZ, working with SME's and owener-managed businesses who want to grow their business further.
Purpose:
Ultimately to get NZ-based business owners to give us their email addresses so that we can market to them.
To be promoted via our communications with clients and into the databases of strategic partners, as well as using google ads to promote more widely.
Target market:
Owners of businesses that are hitting the $1M (or so) turnover mark and who want to grow further. But they are finding that their business has reaching a level of complexity that requires them to start thinking about it differently, and requiring them to get off the tools and out of the way of the growing and developing team. Chances are, they have been in charge of everything that happens in the business thus far and are now working harder than the ever expected to and work/life balance has gone out the window.
KPW Brand Promise:
We talk your language.
KPW Goal:
To change the world’s view of accountants. By that we mean that we do not want to conform to the stereotype, and that our approach will be professional, but not too serious.

```html
<!DOCTYPE html>
<html lang="en">
<head>
<meta charset="utf-8">
<title>The 5 Quiet Leaks that will Sink your Venture – Book Cover</title>
<link rel="stylesheet" href="https://fonts.googleapis.com/css2?family=Oswald:wght@500;600&family=Arimo:wght@400;700&display=swap">
<style>
  :root {
    --backdrop: #ececec;
    --cover-black: #000000;
    --signal-red: #ed1c24;
    --paper-white: #ffffff;
  }
  html, body {
    margin: 0;
    padding: 0;
    width: 1200px;
    height: 1200px;
    overflow: hidden;
    background: var(--backdrop);
  }
  .canvas {
    position: relative;
    width: 1200px;
    height: 1200px;
  }
  .book-cover {
    position: absolute;
    left: 276px;
    top: 82px;
    width: 648px;
    height: 1035px;
    display: block;
  }
  .cover-ground { fill: var(--cover-black); }
  .headline { font-family: "Oswald", "Arial Narrow", sans-serif; font-weight: 500; }
  .big-numeral { font-family: "Oswald", "Arial Narrow", sans-serif; font-weight: 600; fill: var(--signal-red); }
  .accent { fill: var(--signal-red); }
  .plain { fill: var(--paper-white); }
  .the-tab { fill: var(--signal-red); }
  .the-label { font-family: "Arimo", Arial, sans-serif; font-weight: 700; fill: var(--paper-white); }
  .brand-name { font-family: "Oswald", "Arial Narrow", sans-serif; font-weight: 500; fill: var(--paper-white); }
  .author-name { font-family: "Arimo", Arial, sans-serif; font-weight: 400; fill: var(--paper-white); }
</style>
</head>
<body>
<main class="canvas">
  <svg class="book-cover" viewBox="0 0 648 1035" xmlns="http://www.w3.org/2000/svg" role="img" aria-label="Book cover: The 5 Quiet Leaks that will Sink your Venture">
    <rect class="cover-ground" x="0" y="0" width="648" height="1035"/>

    <text class="big-numeral" x="40" y="603" font-size="695" textLength="190" lengthAdjust="spacingAndGlyphs">5</text>

    <rect class="the-tab" x="40" y="40" width="171" height="59"/>
    <text class="the-label" x="56" y="89" font-size="56">THE</text>

    <text class="brand-name" x="585" y="84" font-size="40" text-anchor="end">KPW</text>

    <g class="title-block headline">
      <text class="plain" x="575" y="418" font-size="112" text-anchor="end" textLength="272" lengthAdjust="spacingAndGlyphs">Quiet</text>
      <text class="accent" x="292" y="520" font-size="88" textLength="150" lengthAdjust="spacingAndGlyphs">Leaks</text>
      <text class="plain" x="452" y="520" font-size="64" textLength="120" lengthAdjust="spacingAndGlyphs">that</text>
      <text class="plain" x="232" y="603" font-size="62" textLength="82" lengthAdjust="spacingAndGlyphs">will</text>
      <text class="accent" x="324" y="763" font-size="290" textLength="261" lengthAdjust="spacingAndGlyphs">Sink</text>
      <text class="plain" x="176" y="860" font-size="100" textLength="409" lengthAdjust="spacingAndGlyphs">your Venture</text>
    </g>

    <text class="author-name" x="324" y="996" font-size="37" text-anchor="middle">Author Name</text>
  </svg>
</main>
</body>
</html>
```